Awesome business card design needed

We need a new business card design to go with our new logo.
We are a web development agency that specialises in highly complex back-end integrations as opposed to design, our customers are retailers, hotels, hospitals and any other organisation that has a large online marketing department.
Take a look at our website - www.orvekplus.com for some inspiration.
We want our new business cards to exude class, professionalism and style.
We are likely to choose a high-end card to print them on but we want the design of the card itself to really turn heads.
We have no specific colour requirements, the logo as you will see is a turquoise colour R89 G171 B167 #59aba7 but it can also be in white if you want to make the colour of the card something different.
The information on the card should be:
Name
Position
Tel
email
Potentially a double sided card could have our web address, twitter and FB links.

```html
<!DOCTYPE html>
<html lang="en">
<head>
<meta charset="utf-8">
<title>Orvekplus Business Card</title>
<link rel="stylesheet" href="https://fonts.googleapis.com/css2?family=Open+Sans:wght@400;600;700&display=swap">
<style>
  :root {
    --turquoise: #59aba7;
    --turquoise-dark: #3f8f8b;
    --paper: #ffffff;
    --ink: #3a3a3a;
    --ink-soft: #6a6a6a;
    --backdrop: #ecebe8;
    --social-tile: #3e6fa8;
    --social-tile-2: #4aa6d8;
  }
  * { box-sizing: border-box; margin: 0; padding: 0; }
  html, body { width: 1200px; height: 720px; overflow: hidden; }
  body {
    background: var(--backdrop);
    font-family: "Open Sans", Arial, sans-serif;
    position: relative;
  }
  .card {
    position: absolute;
    top: 205px;
    width: 540px;
    height: 310px;
    border-radius: 4px;
    box-shadow: 0 2px 10px rgba(0,0,0,0.12);
    overflow: hidden;
  }
  /* Front side */
  .card--front { left: 40px; background: var(--paper); }
  .card--front .wordmark {
    position: absolute;
    left: 36px; top: 34px;
    font-size: 66px;
    font-weight: 700;
    letter-spacing: 1px;
    color: var(--turquoise);
    line-height: 1;
  }
  .holder { position: absolute; left: 38px; top: 200px; }
  .holder__name { font-size: 17px; font-weight: 700; color: var(--turquoise); }
  .holder__role { font-size: 12px; color: var(--ink-soft); margin-top: 2px; }
  .card--front .website {
    position: absolute; left: 38px; bottom: 24px;
    font-size: 12px; font-weight: 700; letter-spacing: 2px; color: var(--ink);
  }
  .divider {
    position: absolute; left: 330px; top: 150px;
    width: 1px; height: 112px; background: var(--turquoise);
  }
  .contact { position: absolute; left: 346px; top: 150px; list-style: none; font-size: 12px; color: var(--ink); }
  .contact li { display: flex; align-items: center; gap: 7px; margin-bottom: 8px; }
  .contact svg { width: 11px; height: 11px; flex: none; }
  .contact .address { display: block; margin-top: 14px; line-height: 1.45; }
  /* Back side */
  .card--back { left: 620px; background: var(--turquoise); color: var(--paper); text-align: center; }
  .card--back .wordmark {
    margin-top: 82px;
    font-size: 78px; font-weight: 700; letter-spacing: 1px; line-height: 1;
  }
  .follow { margin-top: 36px; display: flex; justify-content: center; align-items: center; gap: 8px; font-size: 15px; }
  .follow__tile { width: 26px; height: 26px; border-radius: 4px; background: var(--social-tile); }
  .follow__tile--alt { background: var(--social-tile-2); }
  .card--back .website { margin-top: 12px; font-size: 15px; letter-spacing: 2px; }
</style>
</head>
<body>
  <section class="card card--front" aria-label="Card front">
    <div class="wordmark">orvekplus</div>
    <div class="holder">
      <p class="holder__name">Your Name</p>
      <p class="holder__role">Position</p>
    </div>
    <p class="website">www.orvekplus.com</p>
    <div class="divider"></div>
    <ul class="contact">
      <li>
        <svg viewBox="0 0 12 12" aria-hidden="true"><circle cx="6" cy="6" r="6" fill="var(--turquoise)"/><path d="M4 3.2c.4-.3.8 0 1 .5l.2.6c.1.3-.3.6-.3.6.3.7.8 1.2 1.4 1.5 0 0 .3-.4.6-.3l.6.2c.5.2.7.6.4 1-.6.8-2.4.4-3.4-.8C3.5 5.4 3.3 3.8 4 3.2z" fill="#fff"/></svg>
        123-456-7890
      </li>
      <li>
        <svg viewBox="0 0 12 12" aria-hidden="true"><circle cx="6" cy="6" r="6" fill="var(--turquoise)"/><rect x="3" y="4" width="6" height="4.2" fill="#fff"/><path d="M3 4l3 2.3L9 4" stroke="var(--turquoise)" stroke-width=".7" fill="none"/></svg>
        info@orvekplus.com
      </li>
      <li class="address">Street Name, City Name<br>State Zip Code</li>
    </ul>
  </section>

  <section class="card card--back" aria-label="Card back">
    <div class="wordmark">orvekplus</div>
    <div class="follow">
      <span>Follow Us On:</span>
      <span class="follow__tile" aria-label="Social profile one"></span>
      <span class="follow__tile follow__tile--alt" aria-label="Social profile two"></span>
    </div>
    <p class="website">www.orvekplus.com</p>
  </section>
</body>
</html>
```